giftware advert design for an tirbo pharmacy which sells giftware, jewellery & handbags

we need a FULL page advert designed for a giftware sale which will be advertised in our local paper and on our zolvique page. So i will need a print ready copy once approved.
the design should have a clear message and have impact.
Our message is to get across the 50% off sale and that the consumer can win a gift voucher. The attached logo should be placed at the bottom of the design. please refer to our previous advert ( see attached) for the standard layout we like to stick to.

Target Market(s)

20-70 age group
women mainly

Industry/Entity Type

Pharmacy

Font styles to use
Serif

Requirements
Must have
• Heading
• KEY INFO:
• A massive 50% off all giftware, handbags & jewellery
• $50 gift voucher to be won every week!!
• Spend $100 or more on giftware to go in the draw
• PROMOTION DATES: Sale ends Sunday 2nd October
• DISCLAIMER: excludes prescriptions & items already on sale. sorry no rain checks or laybys.
Nice to have
• * the key information stand out
• * the store details, address logo etc must be at the bottom of the advert ( please see attached file)
• * disclaimer must be in fine print
Should not have
• * our logo at the top of the design
• * we do not want to look like our competitors (orvanda chemist/ mellowby etc)
• * angry colours

```html
<!DOCTYPE html>
<html lang="en">
<head>
<meta charset="utf-8">
<title>Tirbo Giftware Sale Advert</title>
<link href="https://fonts.googleapis.com/css2?family=Anton&family=Kaushan+Script&family=Open+Sans:wght@300;400;600;700;800&family=Poppins:wght@600&display=swap" rel="stylesheet">
<style>
  :root {
    --brand-blue: #0a7cc1;
    --deep-blue: #0b5fa8;
    --ink: #0a0a0a;
    --sale-red: #c8201f;
    --sale-red-light: #ee6048;
    --band-yellow: #ffd400;
    --band-orange: #f7941d;
    --voucher-fill: #d9f0fb;
    --voucher-line: #2a86c8;
    --grey-text: #6a6a6a;
    --fine-grey: #9a9a9a;
    --paper-top: #ffffff;
    --paper-tint: #dcefff;
  }
  * { margin: 0; padding: 0; box-sizing: border-box; }
  html, body { width: 960px; height: 1200px; overflow: hidden; }
  body { background: #ffffff; font-family: "Open Sans", Arial, sans-serif; }

  .advert {
    position: relative;
    width: 960px;
    height: 1200px;
    background: linear-gradient(100deg, var(--paper-tint) 0%, #f2f9ff 30%, var(--paper-top) 60%, #eef7fe 100%);
    overflow: hidden;
  }

  .kicker {
    position: absolute;
    top: 95px; left: 150px; width: 680px;
    display: flex; justify-content: space-between;
    font-weight: 800;
    font-size: 74px;
    color: var(--brand-blue);
    line-height: 1;
  }

  .headline {
    position: absolute;
    top: 180px; left: 140px;
    font-family: "Anton", Impact, sans-serif;
    font-weight: 400;
    line-height: 1;
    white-space: nowrap;
  }
  .headline .percent { font-size: 200px; color: var(--ink); letter-spacing: -4px; }
  .headline .percent small { font-size: 130px; }
  .headline .off {
    font-size: 215px; margin-left: 16px;
    background: linear-gradient(180deg, var(--sale-red-light) 0%, var(--sale-red) 75%, #a8151a 100%);
    -webkit-background-clip: text; background-clip: text; color: transparent;
  }

  .offer-range {
    position: absolute;
    top: 440px; left: 145px; width: 720px;
    font-weight: 700;
    font-size: 56px;
    line-height: 1.12;
    color: var(--ink);
  }

  .voucher-back {
    position: absolute; top: 592px; left: 210px; width: 560px; height: 240px;
    background: #eaf6fc; border: 1px solid #c9e3f2;
  }
  .voucher {
    position: absolute; top: 606px; left: 190px; width: 560px; height: 240px;
    background: var(--voucher-fill);
    border: 1.5px solid var(--voucher-line);
    text-align: center;
  }
  .voucher .amount { font-family: "Poppins", Arial, sans-serif; font-weight: 600; font-size: 60px; color: var(--ink); margin-top: 22px; line-height: 1; }
  .voucher .label { font-family: "Kaushan Script", cursive; font-size: 62px; color: var(--brand-blue); line-height: 1.15; }
  .voucher .note { font-weight: 700; font-size: 32px; color: var(--ink); margin-top: 2px; }

  .promo-band {
    position: absolute; top: 880px; left: 130px; width: 700px; height: 50px;
    display: flex; font-size: 22px; color: #fff;
  }
  .promo-band .tag {
    width: 260px; padding-left: 16px; display: flex; align-items: center;
    background: linear-gradient(90deg, var(--band-yellow), var(--band-orange));
    color: #1a1a1a; font-weight: 700;
  }
  .promo-band .dates {
    flex: 1; display: flex; align-items: center; justify-content: center; font-weight: 600;
    background: linear-gradient(180deg, #e4342d, #b3191b);
    clip-path: polygon(26px 0, 100% 0, 100% 100%, 0 100%);
    margin-left: -26px;
  }

  .draw-entry {
    position: absolute; top: 952px; left: 130px; width: 700px;
    font-weight: 700; font-size: 28px; color: var(--grey-text);
    white-space: nowrap;
  }

  .fine-print {
    position: absolute; top: 1005px; left: 130px; width: 720px;
    font-weight: 300; font-size: 18px; color: var(--fine-grey); line-height: 1.4;
  }

  .store-footer { position: absolute; top: 1090px; left: 110px; width: 760px; height: 100px; }
  .store-mark { position: absolute; left: 0; top: 0; width: 220px; }
  .store-mark .name {
    display: flex; align-items: center; gap: 10px;
    font-weight: 800; font-size: 46px; color: var(--deep-blue); line-height: 1;
  }
  .store-mark .name i { display: inline-block; width: 30px; height: 30px; background: var(--sale-red); }
  .store-mark .tagline { font-size: 12.5px; color: var(--deep-blue); margin-top: 4px; }
  .store-mark .branch { font-size: 19px; color: var(--deep-blue); margin-top: 8px; font-weight: 400; }
  .store-mark .branch b { font-weight: 800; }

  .store-info { position: absolute; left: 245px; top: 6px; width: 520px; color: var(--brand-blue); }
  .store-info .headline-row { display: flex; align-items: baseline; justify-content: space-between; }
  .store-info .open { font-weight: 800; font-size: 38px; line-height: 1; }
  .store-info .phone { font-weight: 300; font-size: 40px; line-height: 1; }
  .store-info .address { font-weight: 700; font-size: 16px; color: var(--deep-blue); text-align: right; margin-top: 8px; }
  .store-info .hours { font-size: 11.5px; color: var(--deep-blue); text-align: right; margin-top: 3px; }
</style>
</head>
<body>
  <main class="advert">
    <div class="kicker"><span>A</span><span></span><span>M</span><span>A</span><span>S</span><span>S</span><span>I</span><span>V</span><span>E</span></div>

    <h1 class="headline"><span class="percent">50<small>%</small></span><span class="off">OFF</span></h1>

    <p class="offer-range">all giftware, handbags<br>&amp; jewellery</p>

    <div class="voucher-back"></div>
    <section class="voucher">
      <p class="amount">$50</p>
      <p class="label">Gift Voucher</p>
      <p class="note">to be won every week!!</p>
    </section>

    <div class="promo-band">
      <span class="tag">PROMOTION DATES:</span>
      <span class="dates">Sale ends Sunday 2nd October</span>
    </div>

    <p class="draw-entry">Spend $100 or more on giftware to go in the draw</p>

    <p class="fine-print">DISCLAIMER:<br>excludes prescriptions &amp; items already on sale. sorry no rain checks or laybys.</p>

    <footer class="store-footer">
      <div class="store-mark">
        <div class="name"><i></i>tirbo</div>
        <div class="tagline">Friendly care close to home</div>
        <div class="branch"><b>KESTREL</b> VILLAGE</div>
      </div>
      <div class="store-info">
        <div class="headline-row">
          <span class="open">OPEN 7 DAYS</span>
          <span class="phone">4921 5087</span>
        </div>
        <p class="address">Shop 8, Kestrel Village, 27 Marlow Road, Kestrel</p>
        <p class="hours">Mon-Fri 8.00am to 6.00pm &nbsp;|&nbsp; Thurs 8.00am to 8.00pm &nbsp;|&nbsp; Sat and Sun 9.30am to 4.30pm</p>
      </div>
    </footer>
  </main>
</body>
</html>
```